ONLINE MATTRESS COMPANY REQUIRING BOX DESIGN FOR MATTRESS IN A BOX

WE NEED A BOX DESIGN FOR A NEW COMPANY THAT SELLS A MATTRESS IN A BOX (SIMILAR TO QUILVANO.COM) THAT INCORPORATES ONLY 2 COLOURS (TEAL & BLACK) THE BASE COLOUR OF BOX IS WHITE. THE DESIGN HAS TO INSPIRE MILLENNIAL AND YOUNG SHOPPERS TO WANT TO PURCHASE THE PRODUCT. BOX SHOULD BE SIMPLE AND CLEAN. ONE SIDE HAS TO SHOW THE OPENING INSTRUCTIONS WHICH ARE ATTACHED IN A SAMPLE BOX.

Target Market(s)

MILLENNIALS

Industry/Entity Type

Furniture Store

Font styles to use
Serif
Sans Serif

Colors
ffffff
33b8a4

Requirements
Must have
• ONE SIDE MUST HAVE OPEN INSTRUCTIONS (SEE EXAMPLE); THE FACTORY CAN ONLY PRING ON A WHITE BOX WITH 2 COLOURS. THE WRITING AND SHAPES CAN BE TEAL AND BLACK BUT THE WHOLE BOX CANNOT BE TEAL AND BLACK, JUST THE ART WORK.
Should not have
• CAN ONLY BE 2 COLOURS; BOX COLOUR IS WHITE ; TEAL & BLACK AS OTHER INK COLOURS.

SHOULD NOT SHOW LOGO VERTICALLY (UP AND DOWN) BECAUSE IT IS HARD TO READ, SHOULD BE HORIZONTAL.

DO NOT SHOW MATTRESS OR PILLOW ON BOX IT'S ONLY TO HELP GUIDE YOU SO KNOW WHAT THE PRODUCT IS!

```html
<!DOCTYPE html>
<html lang="en">
<head>
<meta charset="utf-8">
<title>Nolva Hybrid Mattress Box Panels</title>
<link href="https://fonts.googleapis.com/css2?family=Raleway:wght@300;400;500;600&family=Montserrat:wght@700;800&display=swap" rel="stylesheet">
<style>
  :root {
    --teal: #1fb0a6;
    --ink: #141414;
    --white: #ffffff;
    --ground: #e4e4e4;
    --edge: #d2d2d2;
    --icon-fill: #eef3f2;
  }
  * { box-sizing: border-box; margin: 0; padding: 0; }
  html, body { width: 1200px; height: 1200px; overflow: hidden; }
  body {
    background: var(--ground);
    font-family: "Raleway", sans-serif;
    color: var(--ink);
    position: relative;
  }
  .dieline {
    position: absolute;
    left: 80px; top: 100px;
    width: 1040px; height: 1000px;
    display: flex;
    box-shadow: 0 10px 30px rgba(0,0,0,0.08);
  }
  .panel {
    position: relative;
    height: 100%;
    background: var(--white);
    border-right: 1px solid var(--edge);
    overflow: hidden;
  }
  .panel:last-child { border-right: none; }
  .panel--side { width: 230px; }
  .panel--face { width: 290px; }

  .panel__band {
    position: absolute;
    left: 0; right: 0; top: 170px;
    height: 12px;
    background: var(--teal);
  }
  .site-address {
    position: absolute;
    top: 78px; left: 0; right: 0;
    text-align: center;
    font-weight: 300;
    font-size: 34px;
    letter-spacing: 0.5px;
  }
  .brand-name {
    position: absolute;
    top: 62px; left: 0; right: 0;
    text-align: center;
    font-weight: 600;
    font-size: 56px;
    color: var(--teal);
    letter-spacing: 1px;
  }

  /* vertical product copy */
  .side-copy {
    position: absolute;
    top: 230px; bottom: 60px;
    left: 0; right: 0;
    display: flex;
    justify-content: center;
    gap: 14px;
  }
  .side-copy__col {
    writing-mode: vertical-rl;
    white-space: nowrap;
  }
  .side-copy--down { flex-direction: row-reverse; }
  .side-copy--up { transform: rotate(180deg); align-items: flex-start; }
  .side-copy__size {
    font-weight: 500;
    font-size: 46px;
    letter-spacing: 0.5px;
  }
  .side-copy__line {
    display: flex;
    align-items: center;
    gap: 12px;
  }
  .side-copy__hybrid {
    font-weight: 300;
    font-size: 26px;
    letter-spacing: 12px;
  }
  .side-copy__blend {
    font-family: "Montserrat", sans-serif;
    font-weight: 800;
    font-size: 17px;
  }
  .plus { color: var(--teal); }

  /* front face */
  .product-title {
    position: absolute;
    top: 262px; left: 0; right: 0;
    text-align: center;
  }
  .product-title__hybrid {
    font-weight: 300;
    font-size: 40px;
    letter-spacing: 14px;
    margin-right: -14px;
  }
  .product-title__type {
    font-weight: 400;
    font-size: 46px;
    margin-top: 6px;
    letter-spacing: -0.5px;
  }
  .product-title__blend {
    font-family: "Montserrat", sans-serif;
    font-weight: 800;
    font-size: 28px;
    margin-top: 10px;
  }

  /* instructions */
  .setup {
    position: absolute;
    top: 270px; left: 0; right: 0;
    text-align: center;
  }
  .setup__heading {
    font-family: "Montserrat", sans-serif;
    font-weight: 700;
    font-size: 19px;
    margin-bottom: 22px;
  }
  .setup__steps { list-style: none; }
  .setup-step {
    height: 128px;
    display: flex;
    flex-direction: column;
    align-items: center;
  }
  .setup-step__icon { width: 76px; height: 72px; }
  .setup-step__text {
    font-size: 10px;
    font-weight: 500;
    line-height: 1.25;
    margin-top: 6px;
    max-width: 190px;
  }
</style>
</head>
<body>
  <main class="dieline">

    <section class="panel panel--side">
      <p class="site-address">nolva.ca</p>
      <div class="panel__band"></div>
      <div class="side-copy side-copy--down">
        <p class="side-copy__col side-copy__size">QUEEN SIZE MATTRESS</p>
        <p class="side-copy__col side-copy__line">
          <span class="side-copy__hybrid">HYBRID</span>
          <span class="side-copy__blend">GEL <span class="plus">+</span> BAMBOO</span>
        </p>
      </div>
    </section>

    <section class="panel panel--face">
      <p class="brand-name">nolva</p>
      <div class="panel__band"></div>
      <div class="product-title">
        <p class="product-title__hybrid">HYBRID</p>
        <p class="product-title__type">MATTRESS</p>
        <p class="product-title__blend">GEL <span class="plus">+</span> BAMBOO</p>
      </div>
    </section>

    <section class="panel panel--side">
      <p class="site-address">nolva.ca</p>
      <div class="panel__band"></div>
      <div class="side-copy side-copy--up">
        <p class="side-copy__col side-copy__line">
          <span class="side-copy__hybrid">HYBRID</span>
          <span class="side-copy__blend">GEL <span class="plus">+</span> BAMBOO</span>
        </p>
        <p class="side-copy__col side-copy__size">QUEEN SIZE MATTRESS</p>
      </div>
    </section>

    <section class="panel panel--face">
      <p class="brand-name">nolva</p>
      <div class="panel__band"></div>
      <div class="setup">
        <h2 class="setup__heading">HOW TO SET UP</h2>
        <ol class="setup__steps">
          <li class="setup-step">
            <svg class="setup-step__icon" viewBox="0 0 76 72" role="img" aria-label="Line drawing of a box being opened from the top">
              <circle cx="42" cy="38" r="31" fill="var(--icon-fill)" stroke="var(--ink)" stroke-width="2.5"/>
              <circle cx="13" cy="11" r="9" fill="var(--teal)"/>
              <text x="13" y="15" text-anchor="middle" font-family="Raleway, sans-serif" font-size="12" font-weight="600" fill="var(--ink)">1</text>
            </svg>
            <p class="setup-step__text">Open the box from the top and lay it on it's side to pull out the mattress.</p>
          </li>
          <li class="setup-step">
            <svg class="setup-step__icon" viewBox="0 0 76 72" role="img" aria-label="Line drawing of a mattress unrolling">
              <circle cx="42" cy="38" r="31" fill="var(--icon-fill)" stroke="var(--ink)" stroke-width="2.5"/>
              <circle cx="13" cy="11" r="9" fill="var(--teal)"/>
              <text x="13" y="15" text-anchor="middle" font-family="Raleway, sans-serif" font-size="12" font-weight="600" fill="var(--ink)">2</text>
            </svg>
            <p class="setup-step__text">Allow your mattress to unfold and expand slowly.</p>
          </li>
          <li class="setup-step">
            <svg class="setup-step__icon" viewBox="0 0 76 72" role="img" aria-label="Line drawing of a flat mattress with a timer">
              <circle cx="42" cy="38" r="31" fill="var(--icon-fill)" stroke="var(--ink)" stroke-width="2.5"/>
              <circle cx="13" cy="11" r="9" fill="var(--teal)"/>
              <text x="13" y="15" text-anchor="middle" font-family="Raleway, sans-serif" font-size="12" font-weight="600" fill="var(--ink)">3</text>
            </svg>
            <p class="setup-step__text">You can use your mattress 2-4 hours after opening but may need 24-48 hours for optimum expansion and comfort.</p>
          </li>
          <li class="setup-step">
            <svg class="setup-step__icon" viewBox="0 0 76 72" role="img" aria-label="Recycling symbol drawing">
              <circle cx="42" cy="38" r="31" fill="var(--icon-fill)" stroke="var(--ink)" stroke-width="2.5"/>
              <circle cx="13" cy="11" r="9" fill="var(--teal)"/>
              <text x="13" y="15" text-anchor="middle" font-family="Raleway, sans-serif" font-size="12" font-weight="600" fill="var(--ink)">4</text>
            </svg>
            <p class="setup-step__text">Recycle the box and do your little bit for the planet.</p>
          </li>
          <li class="setup-step">
            <svg class="setup-step__icon" viewBox="0 0 76 72" role="img" aria-label="Line drawing of a person resting on a mattress">
              <circle cx="42" cy="38" r="31" fill="var(--icon-fill)" stroke="var(--ink)" stroke-width="2.5"/>
              <circle cx="13" cy="11" r="9" fill="var(--teal)"/>
              <text x="13" y="15" text-anchor="middle" font-family="Raleway, sans-serif" font-size="12" font-weight="600" fill="var(--ink)">5</text>
            </svg>
            <p class="setup-step__text">Now its time to relax and get a great night's sleep!</p>
          </li>
        </ol>
      </div>
    </section>

  </main>
</body>
</html>
```